Design (no text) for 7 pages of Wordpress website

I need seven of the pages on a website re-designed. The website is using Wordpress as the platform.

The text on the pages can remain unchanged.

The site is for outdoor markets, events.

Industry/Entity Type

Events, markets, fairs

Number of Pages Required

5+ page

Colors
00AB8E
00BBA5
67D7C9
C6EFE9
E9F9F6
EE7325
F08F49
F5BC92
FAE3D3
FDF4ED

```html
<!DOCTYPE html>
<html lang="en">
<head>
<meta charset="utf-8">
<title>Gumtree Flat Markets – page designs</title>
<link href="https://fonts.googleapis.com/css2?family=Roboto:wght@300;400;500;700&family=Roboto+Condensed:wght@400;700&display=swap" rel="stylesheet">
<style>
:root{
  --teal:#00AB8E; --teal-2:#00BBA5; --teal-3:#67D7C9; --teal-4:#C6EFE9; --teal-5:#E9F9F6;
  --orange:#EE7325; --orange-2:#F08F49; --orange-3:#F5BC92;
  --ink:#222; --muted:#666; --stage:#c9c9c9; --white:#fff;
}
*{box-sizing:border-box;margin:0;padding:0}
html,body{width:1200px;height:3323px;overflow:hidden;background:var(--stage);font-family:"Roboto",sans-serif;color:var(--ink)}
.page{position:absolute;left:133px;width:934px;background:var(--white);box-shadow:0 2px 8px rgba(0,0,0,.15);overflow:hidden}
.page--home{top:105px;height:545px}
.page--visitors{top:764px;height:2422px}
.abs{position:absolute}
/* header */
.header{position:absolute;left:0;top:0;width:934px;height:90px}
.brand{position:absolute;left:86px;top:20px;display:flex;align-items:center;gap:8px;font-family:"Roboto Condensed",sans-serif;font-weight:700;font-size:26px;color:var(--ink)}
.brand__mark{width:16px;height:16px;background:var(--orange)}
.phone{position:absolute;left:481px;top:22px;font-size:10px;font-weight:500;display:flex;align-items:center;gap:5px}
.search{position:absolute;left:682px;top:11px;width:163px;height:30px;display:flex}
.search__field{flex:1;background:#eee;font-size:10px;color:#777;padding:9px 12px}
.search__btn{width:35px;background:var(--orange);display:flex;align-items:center;justify-content:center}
.nav{position:absolute;left:241px;top:64px;display:flex;gap:19px;font-size:10.5px;text-transform:uppercase;color:#333}
.nav .is-active{color:var(--orange)}
/* hero */
.hero{position:absolute;left:0;top:90px;width:934px;height:392px;background:linear-gradient(120deg,#6f7a52,#a58d6b 45%,#c9b39a 70%,#8f9a6a)}
.hero--visitors{background:linear-gradient(110deg,#5c5850,#9d8b78 45%,#d2c2ae 70%,#8c8a86)}
.hero__shade{position:absolute;inset:0;background:rgba(0,0,0,.22)}
.hero__title{position:absolute;left:0;right:0;text-align:center;color:#fff;font-size:41px;font-weight:400;line-height:1}
.btn{display:inline-flex;align-items:center;justify-content:center;height:38px;border-radius:19px;background:var(--orange);color:#fff;font-weight:700;font-size:12.5px;box-shadow:0 2px 6px rgba(0,0,0,.25)}
.dots{position:absolute;left:0;right:0;bottom:28px;display:flex;justify-content:center;align-items:center;gap:7px}
.dot{width:11px;height:11px;border-radius:50%;border:1.5px solid #fff}
.dot--active{width:16px;height:16px;border:2px solid var(--orange)}
/* footer */
.footer{position:absolute;left:0;width:934px;height:80px;background:#fff;text-align:center;font-size:10px;color:#333;padding-top:27px}
/* info */
.info{position:absolute;left:86px;top:391px;width:381px;height:225px;background:var(--orange);color:#fff;font-family:"Roboto Condensed",sans-serif;font-weight:700;font-size:17px;line-height:25px;padding:36px 0 0 59px}
.photo{position:absolute}
.heading-teal{font-family:"Roboto Condensed",sans-serif;font-weight:700;color:var(--teal-2);font-size:25px}
.body-copy{font-size:10px;line-height:17.5px;color:var(--muted)}
.body-copy p{margin-bottom:17px}
.highlight{font-family:"Roboto Condensed",sans-serif;font-weight:700;color:var(--orange);font-size:13.5px;line-height:20px}
/* features */
.features{position:absolute;left:0;top:1183px;width:934px;height:499px;background:var(--teal-4)}
.features__title{position:absolute;top:78px;left:0;right:0;text-align:center;font-family:"Roboto Condensed",sans-serif;font-weight:700;font-size:25px}
.feat{position:absolute;width:300px}
.feat h3{font-family:"Roboto Condensed",sans-serif;font-weight:700;font-size:16px;margin-bottom:8px}
.feat p{font-size:10px;line-height:17.5px;color:var(--muted)}
.feat--left{text-align:right;left:34px}
.feat--right{left:576px}
.icon{position:absolute;width:64px;height:64px;border-radius:50%;background:var(--teal-2);display:flex;align-items:center;justify-content:center}
.section-title{font-family:"Roboto Condensed",sans-serif;font-weight:700;font-size:25px}
/* band */
.band{position:absolute;left:0;top:2148px;width:934px;height:187px;display:flex}
.band__item{flex:1;color:#fff;text-align:center;font-family:"Roboto Condensed",sans-serif;font-weight:700;font-size:15.5px;line-height:20px;padding-top:28px}
.band__item--teal{background:var(--teal-2)}
.band__item--orange{background:var(--orange)}
.band__icon{width:72px;height:72px;border-radius:50%;background:#fff;margin:0 auto 16px;display:flex;align-items:center;justify-content:center}
</style>
</head>
<body>

<!-- Home page -->
<section class="page page--home">
  <header class="header">
    <div class="brand"><span class="brand__mark"></span>MARKETFOLD</div>
    <div class="phone"><svg width="9" height="9" viewBox="0 0 24 24"><path fill="#222" d="M6.6 10.8a15 15 0 0 0 6.6 6.6l2.2-2.2c.3-.3.7-.4 1-.2 1.1.4 2.3.6 3.6.6.6 0 1 .4 1 1V20c0 .6-.4 1-1 1A17 17 0 0 1 3 4c0-.6.4-1 1-1h3.5c.6 0 1 .4 1 1 0 1.3.2 2.5.6 3.6.1.3 0 .7-.2 1z"/></svg>Call us Today : +1 555 010 2030</div>
    <div class="search"><div class="search__field">Search</div><div class="search__btn"><svg width="11" height="11" viewBox="0 0 24 24"><circle cx="10" cy="10" r="6" fill="none" stroke="#fff" stroke-width="3"/><path d="M15 15l6 6" stroke="#fff" stroke-width="3"/></svg></div></div>
    <nav class="nav"><span>Home</span><span>Book a stall</span><span>Stallfinder</span><span class="is-active">Gumtree Flat Markets</span><span>Riverbend Markets</span><span>Contact us</span><span>About us</span></nav>
  </header>
  <div class="hero" role="img" aria-label="Photo of a smiling shopper at a fresh produce stall">
    <div class="hero__shade"></div>
    <h1 class="hero__title" style="top:112px">Gumtree Flat Markets</h1>
    <div class="abs" style="left:344px;top:165px;display:flex;gap:10px">
      <span class="btn" style="width:117px">VISITORS</span>
      <span class="btn" style="width:137px">STALLHOLDERS</span>
    </div>
    <div class="dots"><span class="dot"></span><span class="dot dot--active"></span><span class="dot"></span></div>
  </div>
  <footer class="footer" style="top:482px">© 2021 MARKETFOLD // PRIVACY POLICY // COOKIE POLICY.</footer>
</section>

<!-- Visitor page -->
<section class="page page--visitors">
  <header class="header">
    <div class="brand"><span class="brand__mark"></span>MARKETFOLD</div>
    <div class="phone"><svg width="9" height="9" viewBox="0 0 24 24"><path fill="#222" d="M6.6 10.8a15 15 0 0 0 6.6 6.6l2.2-2.2c.3-.3.7-.4 1-.2 1.1.4 2.3.6 3.6.6.6 0 1 .4 1 1V20c0 .6-.4 1-1 1A17 17 0 0 1 3 4c0-.6.4-1 1-1h3.5c.6 0 1 .4 1 1 0 1.3.2 2.5.6 3.6.1.3 0 .7-.2 1z"/></svg>Call us Today : +1 555 010 2030</div>
    <div class="search"><div class="search__field">Search</div><div class="search__btn"><svg width="11" height="11" viewBox="0 0 24 24"><circle cx="10" cy="10" r="6" fill="none" stroke="#fff" stroke-width="3"/><path d="M15 15l6 6" stroke="#fff" stroke-width="3"/></svg></div></div>
    <nav class="nav"><span>Home</span><span>Book a stall</span><span>Stallfinder</span><span class="is-active">Gumtree Flat Markets</span><span>Riverbend Markets</span><span>Contact us</span><span>About us</span></nav>
  </header>
  <div class="hero hero--visitors" role="img" aria-label="Photo of a stallholder handing a bag to a shopper">
    <div class="hero__shade"></div>
    <h1 class="hero__title" style="top:112px;line-height:41px">Gumtree Flat Markets<br>Visitor Info</h1>
    <div class="abs" style="left:409px;top:202px"><span class="btn" style="width:117px;font-size:11px">LEARN MORE</span></div>
    <div class="dots"><span class="dot"></span><span class="dot dot--active"></span><span class="dot"></span></div>
  </div>

  <div class="info">
    <svg class="abs" style="left:37px;top:39px" width="11" height="15" viewBox="0 0 12 16"><path fill="#fff" d="M6 0a6 6 0 0 0-6 6c0 4.5 6 10 6 10s6-5.5 6-10a6 6 0 0 0-6-6zm0 8.5A2.5 2.5 0 1 1 6 3.5a2.5 2.5 0 0 1 0 5z"/></svg>
    Every Saturday<br>9am-2pm<br><br>Gumtree Flat – Northvale<br>Parklands Cnr of the Wattle Dr and<br>Banksia Rd, Elmsford
  </div>
  <div class="photo" role="img" aria-label="Photo of a happy visitor giving thumbs up among market tents" style="left:467px;top:391px;width:379px;height:225px;background:linear-gradient(160deg,#8fa3b8,#c9c2b5 45%,#7c6a72)"></div>

  <div class="photo" role="img" aria-label="Photo of a smiling woman carrying a basket of produce" style="left:86px;top:680px;width:361px;height:331px;background:linear-gradient(135deg,#a99f8c,#c7a173 50%,#5d7a3a)"></div>
  <div class="abs" style="left:471px;top:678px;width:380px">
    <h2 class="heading-teal" style="margin-bottom:14px">Love a good Saturday market?</h2>
    <div class="body-copy">
      <p>Then you need to go to the Gumtree Flat Markets.</p>
      <p>Are markets your idea of fun? Want to take the family somewhere that is rich in culture, choice and variety every week of the year?</p>
      <p>Uncover the secret gem of the Northvale Parklands of Elmsford. Set in lush surroundings in a hub of activity and entertainment are variety goods galore. There’s a wonderful selection of fashion, household items, homewares, handmade craft items and more awaiting you.</p>
      <p>Plus, you’ll find a feast of farm fresh produce, artisan foods and all kinds of eclectic favourites in the one place. We attract family favourites across Asian, Middle Eastern and European cuisines and bring them together with products direct from the producers of Northvale.</p>
    </div>
    <p class="highlight" style="margin-left:3px">This is a place for you to meet, eat and find a special treat<br>all at the Gumtree Flat Markets!</p>
  </div>

  <div class="features">
    <h2 class="features__title">What you can expect at the Gumtree Flat:</h2>
    <div class="feat feat--left" style="top:129px"><h3>Food and Coffee</h3><p>Grab a bite and a coffee before, during or after your shopping. We’ll have a variety of cuisines and coffee choices available, so you can try something different each week!</p></div>
    <div class="feat feat--left" style="top:236px"><h3>Kid’s fashion</h3><p>Shop until you drop at Northvale’s newest kid’s clothing location. Forget running all over town or paying hipster chic prices. Find your kid’s fashion here</p></div>
    <div class="feat feat--left" style="top:343px"><h3>Get crafty</h3><p>Nothing beats the beauty and design of quality handmade items. Uncover arts and crafts for all occasions, lovingly made knitwear, patchwork and more</p></div>
    <div class="feat feat--right" style="top:129px"><h3>Pet Friendly</h3><p>Bring your furry friends for a frolick through the sprawling Northvale Parklands, while picking up a treat from one of the pet stalls.</p></div>
    <div class="feat feat--right" style="top:236px"><h3>Fun for the kids</h3><p>Bring the kids to enjoy pony rides, a jumping castle and face painting every Saturday.</p></div>
    <div class="feat feat--right" style="top:343px"><h3>Gourmet Produce</h3><p>Shop a range of quality, gourmet produce and baked goods from olives and preserved lemons, to breads and brownies.</p></div>
    <div class="icon" style="left:376px;top:125px"><svg width="32" height="32" viewBox="0 0 32 32" fill="none" stroke="#fff" stroke-width="1.6"><path d="M6 20h20M8 20a8 6 0 0 1 16 0M7 24h18M20 4l-2 8"/></svg></div>
    <div class="icon" style="left:376px;top:232px"><svg width="32" height="32" viewBox="0 0 32 32" fill="none" stroke="#fff" stroke-width="1.6"><path d="M11 5h10l5 5-3 3v14H9V13l-3-3z"/></svg></div>
    <div class="icon" style="left:376px;top:339px"><svg width="32" height="32" viewBox="0 0 32 32" fill="none" stroke="#fff" stroke-width="1.6"><circle cx="16" cy="16" r="5"/><path d="M16 3v6M16 23v6M3 16h6M23 16h6M7 7l4 4M21 21l4 4M25 7l-4 4M11 21l-4 4"/></svg></div>
    <div class="icon" style="left:494px;top:125px"><svg width="32" height="32" viewBox="0 0 32 32" fill="none" stroke="#fff" stroke-width="1.6"><path d="M16 27s-10-6-10-13a5 5 0 0 1 10-2 5 5 0 0 1 10 2c0 7-10 13-10 13z"/></svg></div>
    <div class="icon" style="left:494px;top:232px"><svg width="32" height="32" viewBox="0 0 32 32" fill="none" stroke="#fff" stroke-width="1.6"><circle cx="16" cy="8" r="3"/><path d="M16 11v9M9 14l7 2 7-2M12 28l4-8 4 8"/></svg></div>
    <div class="icon" style="left:494px;top:339px"><svg width="32" height="32" viewBox="0 0 32 32" fill="none" stroke="#fff" stroke-width="1.6"><circle cx="16" cy="13" r="8"/><path d="M12 27h8M14 21v6M18 21v6"/></svg></div>
  </div>

  <div class="abs" style="left:86px;top:1758px;width:381px">
    <h2 class="section-title" style="margin-bottom:14px">We are family-friendly fun</h2>
    <div class="body-copy">
      <p>Where else can you meet your neighbours, find items at op shop prices, meet the farmer and the food maker, all while keeping the whole family entertained?</p>
      <p>Our markets held in the glorious Northvale Parklands, an oasis of greenery and community in the City of Greenfield. You can spend the day browsing fashion, handmade craft items, bric-a-brac, toys, fantastic produce and food from around the globe. Op shop through items new and old with your family every weekend.</p>
      <p>It’s an ever-changing variety of options. 50% of our market stalls change on a week by week basis, so you can always find a new treasure.</p>
      <p>The Northvale Parklands are there for you to enjoy. There’s live entertainment, special events, food festivals and more held on the grounds. You can come for the op shopping and retail therapy and picnic and relax later with a stroll about the Parklands.</p>
    </div>
  </div>
  <div class="photo" role="img" aria-label="Photo of a woman choosing vegetables with a wicker basket" style="left:486px;top:1765px;width:362px;height:303px;background:linear-gradient(135deg,#7d8a86,#b3b7b5 45%,#6f8f3d 80%,#c0473a)"></div>

  <div class="band">
    <div class="band__item band__item--teal"><div class="band__icon"><svg width="42" height="42" viewBox="0 0 42 42" fill="none" stroke="var(--teal-2)" stroke-width="1.6"><circle cx="21" cy="21" r="17"/><path d="M21 10v11l7 5"/></svg></div>Gumtree Flat markets are open every<br>Saturday from 9am to 2pm.</div>
    <div class="band__item band__item--orange"><div class="band__icon"><svg width="42" height="42" viewBox="0 0 42 42" fill="none" stroke="var(--orange)" stroke-width="1.6"><rect x="10" y="5" width="12" height="12"/><path d="M14 14V8h3a2 2 0 0 1 0 4h-3M16 17v20M20 30l3-6h11l3 6v5H20zM22 35v3M35 35v3"/></svg></div>Enter via Banksia Rd and the<br>Wattle Drive for parking.</div>
    <div class="band__item band__item--teal"><div class="band__icon"><svg width="42" height="42" viewBox="0 0 42 42" fill="none" stroke="var(--teal-2)" stroke-width="1.6"><rect x="14" y="6" width="18" height="26" rx="3"/><path d="M14 18h18M18 32v4M28 32v4M8 10v26"/><circle cx="8" cy="9" r="3"/></svg></div>Public transport is available via a bus<br>stop at the Gumtree Flat entrance.</div>
  </div>
  <footer class="footer" style="top:2335px;height:87px;padding-top:32px">© 2021 MARKETFOLD // PRIVACY POLICY // COOKIE POLICY.</footer>
</section>

</body>
</html>
```